Email Marketing Campaign Brief

We want to do an email marketing campaign around our consulting services. The attached documents provide back ground on our work but additional copy can be found below:

TV7pl is committed to helping you, the educator, make informed buying decisions based on local control and independent reviews through a simple, impartial and an effective approach.
In education, there exists a vast array of educational solutions – such as reading, science, language arts, and math curricula; school-wide reform programs; interventions; after-school programs; and new educational technologies. In the marketplace, providers could, and most do, claim to be able to improve educational outcomes and, in many cases, they all pretend to be supported by evidence. But a cursory review reveals that most evidence consists of poorly designed or advocacy-driven studies with some providers having such inadequate research as could only be described as case studies.

So the problem for State and local education officials is that they must sort through a myriad of such claims to decide which solutions merit consideration for their schools and classrooms. One US official stated the problem saying “many of these practitioners have seen interventions (solutions), introduced with great fanfare as being able to produce dramatic gains, come and go over the years, yielding little in the way of positive and lasting change – a perception confirmed by the flat achievement results over the past 30 years in the Federal Review of Learning Outcomes Survey long-term trend”

TV7pl is a process by which we make you, the educator, the locus of control

OUR Approach:
With four simple, yet highly effective steps, TV7pl guides educators through an informed buying process that’s based on local control and review.

Step 1 — Research, Review, and Evaluation Criteria

Step 2 — Cost / Benefit Analysis

Step 3 — Education Survey & Culture Scan

Step 4 — Negotiation & Representation

Target Market(s)

Education

Industry/Entity Type

Marketing

Font styles to use
Sans Serif

Colors
f9b46a
f37122

Requirements
Must have
• HTML format that can be used in an Email Campaign
Nice to have
• Additional Copy in Word

```html
<!DOCTYPE html>
<html lang="en">
<head>
<meta charset="utf-8">
<title>TV7pl — Research + Policy + Practice</title>
<link href="https://fonts.googleapis.com/css2?family=Montserrat:wght@600;700;800&family=Poppins:wght@300;400;500&display=swap" rel="stylesheet">
<style>
  :root {
    --orange: #f37122;
    --orange-soft: #f9b46a;
    --yellow: #f6c21c;
    --gold: #d9a514;
    --ink: #333333;
    --ink-mid: #555555;
    --muted: #9a9a9a;
    --line: #ececec;
    --circle: #f1f1f1;
    --dark: #2b2b2b;
    --footer: #2f2f2f;
    --white: #ffffff;
  }
  * { margin: 0; padding: 0; box-sizing: border-box; }
  html, body { width: 1200px; height: 3546px; overflow: hidden; background: var(--white); }
  body { position: relative; font-family: "Poppins", Arial, sans-serif; color: var(--ink); }
  .abs { position: absolute; }
  .center { left: 0; width: 1200px; text-align: center; }

  /* header */
  .site-header { top: 0; left: 0; width: 1200px; height: 83px; background: var(--white); }
  .brand { left: 155px; top: 20px; display: flex; align-items: center; gap: 12px; }
  .brand-dot { width: 34px; height: 34px; border-radius: 50%; background: var(--orange); }
  .brand-name { font-family: "Poppins", sans-serif; font-weight: 400; font-size: 40px; color: var(--ink-mid); letter-spacing: 0.5px; }
  .nav a { position: absolute; top: 28px; font-family: "Montserrat", sans-serif; font-weight: 600; font-size: 21px; letter-spacing: 2px; color: var(--ink); text-decoration: none; }
  .nav a.active { color: var(--orange); }

  /* hero */
  .hero { top: 83px; left: 0; width: 1200px; height: 580px;
    background: radial-gradient(ellipse at 30% 40%, #f58a3e 0%, #f06a1f 55%, #e85c15 100%); }
  .hero-title { top: 306px; font-family: "Montserrat", sans-serif; font-weight: 700; font-size: 53px; color: var(--white); letter-spacing: 1px; }
  .hero-sub { top: 389px; font-family: "Poppins", sans-serif; font-weight: 500; font-size: 28px; color: #fcd54a; letter-spacing: 1px; }
  .hero-btn { top: 498px; left: 488px; width: 225px; height: 54px; border-radius: 27px; background: var(--yellow);
    color: var(--white); font-family: "Montserrat", sans-serif; font-weight: 700; font-size: 20px; letter-spacing: 1px;
    display: flex; align-items: center; justify-content: center; }

  /* pillars */
  .pillar { top: 741px; width: 360px; text-align: center; }
  .pillar-icon { width: 134px; height: 134px; border-radius: 50%; background: var(--circle); margin: 0 auto; display: flex; align-items: center; justify-content: center; }
  .pillar-icon.active { background: #f3844a; }
  .pillar-title { margin-top: 52px; font-family: "Montserrat", sans-serif; font-weight: 700; font-size: 28px; color: var(--ink); letter-spacing: 0.5px; }
  .pillar-title.active { color: var(--orange); }
  .pillar-text { width: 240px; margin: 26px auto 0; font-size: 21px; line-height: 36px; font-weight: 300; color: var(--muted); }
  .rule { top: 1154px; left: 0; width: 1200px; height: 2px; background: var(--line); }

  /* welcome */
  .welcome-title { top: 1244px; font-family: "Montserrat", sans-serif; font-weight: 700; font-size: 48px; color: var(--ink); letter-spacing: 1px; }
  .welcome-title span { color: var(--orange); }
  .welcome-bar { top: 1310px; left: 547px; width: 106px; height: 3px; background: var(--orange); }
  .welcome-text { top: 1342px; left: 140px; width: 920px; text-align: center; font-size: 23.5px; line-height: 42px; color: #555; }
  .partner-seal { width: 84px; height: 84px; border-radius: 50%; border: 3px solid #8a8a8a; background: #f4f4f4; top: 1572px; }
  .partner-bar { height: 28px; top: 1702px; background: #9a9a9a; border-radius: 3px; }

  /* video */
  .video { top: 1804px; left: 0; width: 1200px; height: 532px;
    background: linear-gradient(135deg, #3a3a3a 0%, #2b2b2b 55%, #242424 100%); }
  .video-title { top: 2016px; font-family: "Poppins", sans-serif; font-weight: 400; font-size: 36px; color: var(--white); letter-spacing: 2px; }
  .video-title strong { font-family: "Montserrat", sans-serif; font-weight: 700; color: var(--orange); }
  .play { top: 2112px; left: 565px; width: 70px; height: 70px; border-radius: 50%; background: var(--orange); display: flex; align-items: center; justify-content: center; }

  /* program */
  .program-title { top: 2394px; font-family: "Montserrat", sans-serif; font-weight: 800; font-size: 42px; color: var(--ink); letter-spacing: 1.5px; }
  .program-sub { top: 2448px; left: 300px; width: 600px; text-align: center; font-size: 21px; line-height: 36px; color: #8a8a8a; letter-spacing: 0.5px; }
  .step-icon { left: 218px; width: 142px; height: 142px; border-radius: 50%; border: 3px solid #e6e6e6; background: var(--white); display: flex; align-items: center; justify-content: center; }
  .step { left: 404px; width: 620px; }
  .step-title { font-family: "Poppins", sans-serif; font-weight: 500; font-size: 27px; line-height: 38px; }
  .step-list { list-style: none; margin-top: 2px; }
  .step-list li { font-size: 22.5px; line-height: 39.5px; color: #6e6e6e; }
  .step-list li::before { content: "• "; }
  .t-orange { color: var(--orange); }
  .t-grey { color: #6a6a6a; }
  .t-gold { color: var(--gold); }
  .t-dark { color: var(--ink); }

  /* footer */
  .site-footer { top: 3342px; left: 0; width: 1200px; height: 204px; background: var(--footer); }
  .social { top: 3402px; left: 0; width: 1200px; display: flex; justify-content: center; gap: 58px; }
  .social a { color: var(--white); text-decoration: none; font-family: "Montserrat", sans-serif; font-weight: 600; font-size: 21px; letter-spacing: 2px; }
  .copyright { top: 3462px; font-size: 21px; color: var(--white); font-family: "Poppins", sans-serif; font-weight: 500; }
</style>
</head>
<body>

<header class="abs site-header">
  <div class="abs brand"><span class="brand-dot"></span><span class="brand-name">TV7pl</span></div>
  <nav class="nav">
    <a href="#" style="left:632px">RESEARCH</a>
    <a href="#" class="active" style="left:797px">POLICY</a>
    <a href="#" style="left:935px">PRACTICE</a>
  </nav>
</header>

<section class="abs hero" role="img" aria-label="Orange-tinted photo of a pencil cup, alarm clock, glasses and books on a desk"></section>
<h1 class="abs center hero-title">RESEARCH + POLICY + PRACTICE</h1>
<p class="abs center hero-sub">ACTIONABLE RESEARCH IN EDUCATION</p>
<a class="abs hero-btn" href="#">EXPLORE IT!</a>

<section>
  <div class="abs pillar" style="left:120px">
    <div class="pillar-icon">
      <svg width="70" height="50" viewBox="0 0 70 50" fill="none" stroke="#f37122" stroke-width="2.5">
        <path d="M6 42 C14 6, 56 6, 64 42"/>
        <line x1="6" y1="12" x2="64" y2="12"/>
        <rect x="30" y="8" width="10" height="8" fill="#fff"/>
        <circle cx="6" cy="12" r="4" fill="#fff"/><circle cx="64" cy="12" r="4" fill="#fff"/>
        <rect x="2" y="40" width="8" height="8" fill="#fff"/><rect x="60" y="40" width="8" height="8" fill="#fff"/>
      </svg>
    </div>
    <h2 class="pillar-title">RESEARCH</h2>
    <p class="pillar-text">Our agency working on email template Design unique Ideas.</p>
  </div>
  <div class="abs pillar" style="left:420px">
    <div class="pillar-icon active">
      <svg width="60" height="54" viewBox="0 0 60 54" fill="none" stroke="#fff" stroke-width="3">
        <rect x="4" y="4" width="52" height="36" rx="3"/>
        <line x1="30" y1="40" x2="30" y2="48"/><line x1="18" y1="50" x2="42" y2="50"/>
      </svg>
    </div>
    <h2 class="pillar-title active">POLICY</h2>
    <p class="pillar-text">Our agency working on email template Design unique Ideas.</p>
  </div>
  <div class="abs pillar" style="left:720px">
    <div class="pillar-icon">
      <svg width="44" height="62" viewBox="0 0 44 62" fill="none" stroke="#f37122" stroke-width="2.5">
        <path d="M22 3 C32 12, 34 26, 30 42 H14 C10 26, 12 12, 22 3 Z"/>
        <circle cx="22" cy="22" r="5"/>
        <path d="M14 32 L6 44 L14 42 M30 32 L38 44 L30 42"/>
        <path d="M18 48 V56 M22 48 V60 M26 48 V56"/>
      </svg>
    </div>
    <h2 class="pillar-title">PRACTICE</h2>
    <p class="pillar-text">Our agency working on email template Design unique Ideas.</p>
  </div>
</section>
<div class="abs rule"></div>

<section>
  <h2 class="abs center welcome-title">WELCOME TO <span>TV7PL</span></h2>
  <div class="abs welcome-bar"></div>
  <p class="abs welcome-text">TV7pl partners with state and local entities to provide research, policy and practice deliverables that yield high value and actionable results. We offer a unique perspective on gathering data and understanding the policy effect and implications for developing models that yield mission critical change in a community, district or organization.</p>
  <div class="abs partner-seal" style="left:389px"></div>
  <div class="abs partner-seal" style="left:507px;width:110px;border-radius:50%"></div>
  <div class="abs partner-seal" style="left:633px"></div>
  <div class="abs partner-seal" style="left:746px"></div>
  <div class="abs partner-bar" style="left:307px;width:116px"></div>
  <div class="abs partner-bar" style="left:443px;width:124px"></div>
  <div class="abs partner-bar" style="left:587px;width:92px"></div>
  <div class="abs partner-bar" style="left:694px;width:92px"></div>
  <div class="abs partner-bar" style="left:802px;width:120px"></div>
</section>

<section class="abs video" role="img" aria-label="Dark photo of a hand sketching a network of people linked by arrows"></section>
<h2 class="abs center video-title">WATCHING OUR <strong>WORKING VIDEO</strong></h2>
<a class="abs play" href="#" aria-label="Play video">
  <svg width="24" height="26" viewBox="0 0 24 26"><path d="M4 2 L22 13 L4 24 Z" fill="#fff"/></svg>
</a>

<section>
  <h2 class="abs center program-title">PROGRAM IMPLEMENTATION</h2>
  <p class="abs program-sub">INDENDENT REVIEW CONNECTED TO SCHOOL DISTRICT NEED AND STAKEHOLDERS</p>

  <div class="abs step-icon" style="top:2552px">
    <svg width="70" height="70" viewBox="0 0 70 70" fill="none" stroke="#e07a12" stroke-width="6">
      <circle cx="42" cy="28" r="18"/><line x1="29" y1="41" x2="10" y2="60" stroke-linecap="round" stroke-width="9"/>
    </svg>
  </div>
  <div class="abs step" style="top:2542px">
    <h3 class="step-title t-orange">Research, Review and Evalutation Criteria</h3>
    <ul class="step-list"><li>District needs analysis</li><li>Program reviews and alignment to need</li><li>independent evaluation / data informed decision</li></ul>
  </div>

  <div class="abs step-icon" style="top:2748px">
    <svg width="74" height="74" viewBox="0 0 74 74">
      <g fill="#666">
        <circle cx="37" cy="37" r="24"/>
        <g id="teeth">
          <rect x="31" y="4" width="12" height="14" rx="2"/>
          <rect x="31" y="56" width="12" height="14" rx="2"/>
          <rect x="4" y="31" width="14" height="12" rx="2"/>
          <rect x="56" y="31" width="14" height="12" rx="2"/>
        </g>
        <use href="#teeth" transform="rotate(45 37 37)"/>
      </g>
      <circle cx="37" cy="37" r="11" fill="#fff"/>
    </svg>
  </div>
  <div class="abs step" style="top:2738px">
    <h3 class="step-title t-grey">Cost / Benefits Analsyis</h3>
    <ul class="step-list"><li>District needs analysis</li><li>Program reviews and alignment to need</li><li>independent evaluation / data informed decision</li></ul>
  </div>

  <div class="abs step-icon" style="top:2945px">
    <svg width="76" height="80" viewBox="0 0 76 80" fill="none" stroke="#f0b400" stroke-width="4" stroke-linecap="round">
      <path d="M38 18 C26 18, 20 27, 20 35 C20 43, 28 47, 29 56 H47 C48 47, 56 43, 56 35 C56 27, 50 18, 38 18 Z" fill="#f6c21c"/>
      <rect x="30" y="60" width="16" height="10" rx="2" fill="#999" stroke="#999"/>
      <line x1="38" y1="2" x2="38" y2="10"/><line x1="8" y1="35" x2="14" y2="35"/><line x1="62" y1="35" x2="68" y2="35"/>
      <line x1="15" y1="12" x2="20" y2="17"/><line x1="61" y1="12" x2="56" y2="17"/>
    </svg>
  </div>
  <div class="abs step" style="top:2935px">
    <h3 class="step-title t-gold">Education Survey and Custure Scan</h3>
    <ul class="step-list"><li>District needs analysis</li><li>Program reviews and alignment to need</li><li>independent evaluation / data informed decision</li></ul>
  </div>

  <div class="abs step-icon" style="top:3141px">
    <svg width="82" height="56" viewBox="0 0 82 56">
      <rect x="12" y="4" width="58" height="38" rx="3" fill="#333"/>
      <rect x="17" y="9" width="48" height="28" fill="#fff"/>
      <path d="M2 46 H80 L76 52 H6 Z" fill="#333"/>
    </svg>
  </div>
  <div class="abs step" style="top:3131px">
    <h3 class="step-title t-dark">Negotiation and Representation</h3>
    <ul class="step-list"><li>District needs analysis</li><li>Program reviews and alignment to need</li><li>independent evaluation / data informed decision</li></ul>
  </div>
</section>

<footer class="abs site-footer"></footer>
<nav class="abs social">
  <a href="#">PALSPACE</a>
  <a href="#">CHIRPER</a>
  <a href="#">SNAPFRAME</a>
  <a href="#">SHOTBOARD</a>
</nav>
<p class="abs center copyright">© 2017 All Right Reserved | TV7pl, LLC</p>

</body>
</html>
```